we need an experienced designer to design the tube for our toothpaste

Design guidelines:
1. On the front side, our product logo (‘Q2786’) should be prominent enough.
2. Our brand logo (‘quorlume’) could be small-size and it's just a trademark indeed.

Some information here for your reference:
1. The color of toothpaste cap is white.
2. We hope that the primary color in the design is blue.
3.‘F’ in ‘Q2786’ stands for ‘quorlume’ and ‘fluoride’.
4. We will use aluminum-plastic composite materials to make toothpaste tubes. In addition to the design, we also hope that you can make relevant suggestions on the special requirements of printing.

At last, we hope that you could submit both 2D design and 3D visual effects.

Attachments:

Colors
0094D4
00A9DD
6FCCEA
C7EBF8
E9F6FB

Requirements
Must have
• as attached

```html
<!DOCTYPE html>
<html lang="en">
<head>
<meta charset="utf-8">
<title>Q2786 Orthodontic Toothpaste – Tube Label Layout</title>
<link href="https://fonts.googleapis.com/css2?family=Rubik:wght@500;700;800;900&family=Barlow:wght@400;600;700&family=Oswald:wght@600&family=Questrial&display=swap" rel="stylesheet">
<style>
  :root{
    --blue-deep:#1c4fa3;
    --blue-mid:#1f6cc4;
    --blue-bright:#0a93d6;
    --navy:#0b2a66;
    --fluoride-blue:#1b5aa6;
    --ink:#222;
    --mint-green:#3a9a2a;
    --cap-green:#59b947;
    --guide-red:#e0343c;
    --white:#ffffff;
  }
  *{box-sizing:border-box;margin:0;padding:0}
  html,body{width:1200px;height:1176px;overflow:hidden;background:var(--white)}
  body{position:relative;font-family:"Barlow",sans-serif;color:var(--ink)}

  /* dimension guides */
  .dim{position:absolute;font-family:"Questrial",sans-serif;color:var(--ink);white-space:nowrap}
  .dim-width{left:511px;top:440px;font-size:49px;letter-spacing:1px}
  .dim-small{font-size:16px}
  .guide-h{position:absolute;height:0;border-top:1px dashed var(--guide-red)}
  .guide-v{position:absolute;width:0;border-left:1px dashed var(--guide-red)}
  .vertical{writing-mode:vertical-rl;transform:rotate(180deg)}
  .dim-height{left:130px;top:734px;font-size:60px;line-height:1}
  .cap-side{left:64px;top:649px;font-size:50px;line-height:1;color:var(--cap-green)}

  /* label */
  .label{position:absolute;left:220px;top:548px;width:837px;height:545px;border:2px solid #111;overflow:hidden;background:var(--white)}
  .label-front{position:absolute;left:0;top:0;width:622px;height:100%;
    background:radial-gradient(ellipse at 48% 35%,var(--blue-bright) 0%,var(--blue-mid) 45%,var(--blue-deep) 100%)}
  .bubble-edge{position:absolute;left:585px;top:0;width:70px;height:100%;
    background:linear-gradient(90deg,rgba(255,255,255,0) 0%,rgba(255,255,255,.55) 45%,#fff 100%)}
  .rule{position:absolute;height:1px;background:#555}
  .frame-line{position:absolute;border:1px solid #333}

  .brand{position:absolute;left:26px;top:122px;display:flex;align-items:center;gap:6px;font-family:"Rubik",sans-serif;font-weight:800;font-size:32px;color:var(--white);letter-spacing:-.5px}
  .brand-dot{width:10px;height:10px;border-radius:50%;background:var(--white)}
  .divider{position:absolute;left:211px;top:86px;width:2px;height:104px;background:var(--white)}
  .product{position:absolute;left:228px;top:78px;font-family:"Rubik",sans-serif;font-weight:900;font-size:98px;line-height:1;color:var(--white);letter-spacing:-2px}
  .product-type{position:absolute;left:230px;top:170px;font-family:"Rubik",sans-serif;font-weight:500;font-size:23px;color:var(--white);letter-spacing:.3px}

  .claim-band{position:absolute;left:0;top:213px;width:567px;height:56px;background:var(--navy);border-radius:0 28px 28px 0}
  .claim-text{position:absolute;left:134px;top:221px;font-family:"Rubik",sans-serif;font-weight:500;font-size:16.5px;line-height:21px;color:var(--white)}
  .claim-visual{position:absolute;left:31px;top:196px;width:88px;height:88px;border-radius:50%;
    background:radial-gradient(circle at 50% 45%,#fff 0%,#f6c9cf 55%,#d9e3ee 100%);border:4px solid #b9c6d6}

  .info{position:absolute;left:28px;width:540px;color:var(--white);font-size:14.5px;line-height:18px}
  .pill{display:inline-block;background:var(--navy);border-radius:12px;padding:2px 8px;font-family:"Rubik",sans-serif;font-weight:700;font-size:14px;margin-bottom:3px}

  .side{position:absolute;left:640px;width:186px;text-align:center}
  .fluoride{top:42px;font-family:"Rubik",sans-serif;font-weight:800;font-size:27px;line-height:28px;color:var(--fluoride-blue)}
  .fluoride span{display:block;color:var(--ink)}
  .flavour-visual{position:absolute;left:660px;top:106px;width:150px;height:118px;border-radius:40% 40% 30% 30%;
    background:radial-gradient(ellipse at 50% 40%,#7fc25a 0%,#3f8a2c 60%,#e8eef2 100%)}
  .flavour{top:228px;font-family:"Oswald",sans-serif;font-weight:600;font-size:31px;color:var(--mint-green)}
  .net{top:272px;font-family:"Rubik",sans-serif;font-weight:500;font-size:13px;color:#111}
  .care{top:310px;font-family:"Rubik",sans-serif;font-weight:700;font-size:12.5px;line-height:15.5px;color:var(--fluoride-blue)}
  .orth-visual{position:absolute;top:369px;width:78px;height:78px;border-radius:50%;background:radial-gradient(circle,#f3d2cc 0%,#f7c4ba 60%,#e87f86 100%)}
  .benefits{position:absolute;left:656px;top:483px;list-style:none;font-family:"Rubik",sans-serif;font-weight:700;font-size:12.5px;line-height:18px;color:var(--cap-green)}
  .benefits li{display:flex;align-items:center;gap:9px}
  .benefits svg{width:11px;height:12px}
</style>
</head>
<body>
  <!-- width dimensions -->
  <div class="dim dim-width">147.638mm</div>
  <div class="guide-h" style="left:220px;top:517px;width:837px"></div>
  <div class="guide-v" style="left:220px;top:474px;height:61px"></div>
  <div class="guide-v" style="left:248px;top:474px;height:61px"></div>
  <div class="guide-v" style="left:973px;top:474px;height:61px"></div>
  <div class="guide-v" style="left:1052px;top:474px;height:61px"></div>
  <div class="dim dim-small" style="left:220px;top:490px">5mm</div>
  <div class="dim dim-small" style="left:981px;top:490px">14mm</div>

  <!-- height dimensions -->
  <div class="guide-h" style="left:135px;top:545px;width:78px"></div>
  <div class="guide-h" style="left:135px;top:551px;width:78px"></div>
  <div class="guide-h" style="left:135px;top:1083px;width:78px"></div>
  <div class="guide-h" style="left:135px;top:1093px;width:78px"></div>
  <div class="guide-v" style="left:196px;top:545px;height:548px"></div>
  <div class="guide-v" style="left:211px;top:545px;height:548px"></div>
  <div class="dim dim-small" style="left:148px;top:555px">1mm</div>
  <div class="dim dim-small" style="left:143px;top:1064px">2mm</div>
  <div class="dim vertical dim-height">97mm</div>
  <div class="dim vertical cap-side">tube cap side</div>
  <div class="dim dim-small" style="left:1070px;top:934px">3*8mm</div>

  <!-- flat tube label -->
  <section class="label">
    <div class="label-front"></div>
    <div class="bubble-edge" role="img" aria-label="Column of white bubbles along the edge of the blue panel"></div>
    <div class="rule" style="left:0;top:32px;width:837px;opacity:.5"></div>
    <div class="rule" style="left:0;top:295px;width:837px;opacity:.6"></div>
    <div class="frame-line" style="left:640px;top:6px;width:187px;height:531px;border-left:none"></div>

    <div class="brand"><span>quorlume</span><span class="brand-dot"></span></div>
    <div class="divider"></div>
    <div class="product">Q2786</div>
    <div class="product-type">ORTHODONTIC TOOTHPASTE</div>

    <div class="claim-band"></div>
    <div class="claim-visual" role="img" aria-label="Illustration of a tooth and gum under a magnifying glass"></div>
    <div class="claim-text">Enhanced Cavity Prevention And Gum Protection For<br>Use When Wearing Metal Braces And Clear Aligners</div>

    <div class="info" style="top:310px">
      <span class="pill">DIRECTIONS</span>
      <p>Apply at least one inch strip of the product onto a soft bristle toothbrush. Brush teeth thoroughly, for at least three minutes twice a day.</p>
    </div>
    <div class="info" style="top:383px">
      <span class="pill">INGREDIENTS</span>
      <p>Aqua, Sorbitol, Hydrated Silica, Glycerin, PEG-12, Sodium Lauryl Sulfate, Aroma, Cellulose Gum, Titanium Dioxide, Potassium Sorbate, Allantoin, Sodium Fluoride, Citric Acid, Peppermint Essence, Sodium Saccharin, CI 47005, CI 42090, Cinnamal.</p>
    </div>
    <div class="info" style="top:474px">
      <span class="pill">WARNINGS</span>
      <p>Do not ingest.Keep out of reach of children under 6 years of age.</p>
    </div>

    <div class="side fluoride">FLUORIDE<span>1450 PPM</span></div>
    <div class="flavour-visual" role="img" aria-label="Illustration of fresh mint leaves"></div>
    <div class="side flavour">Frost Mint</div>
    <div class="side net">Net Wt. 85g</div>
    <div class="side care">PREMIUM ORAL CARE<br>DURING ORTHODONTIC<br>TREATMENT</div>
    <div class="orth-visual" style="left:651px" role="img" aria-label="Illustration of teeth with metal braces"></div>
    <div class="orth-visual" style="left:736px" role="img" aria-label="Illustration of teeth with clear aligners"></div>
    <ul class="benefits">
      <li><svg viewBox="0 0 11 12"><path d="M1 2.5C1 .5 3.5 0 5.5 1 7.5 0 10 .5 10 2.5c0 2-1 3-1.3 5-.3 2-.6 4-1.4 4S6.3 8.5 5.5 8.5 4.5 11.5 3.7 11.5 2.6 9.5 2.3 7.5C2 5.5 1 4.5 1 2.5z" fill="currentColor"/></svg>PREVENT CAVITY</li>
      <li><svg viewBox="0 0 11 12"><path d="M1 2.5C1 .5 3.5 0 5.5 1 7.5 0 10 .5 10 2.5c0 2-1 3-1.3 5-.3 2-.6 4-1.4 4S6.3 8.5 5.5 8.5 4.5 11.5 3.7 11.5 2.6 9.5 2.3 7.5C2 5.5 1 4.5 1 2.5z" fill="currentColor"/></svg>FRESHEN BREATH</li>
      <li><svg viewBox="0 0 11 12"><path d="M1 2.5C1 .5 3.5 0 5.5 1 7.5 0 10 .5 10 2.5c0 2-1 3-1.3 5-.3 2-.6 4-1.4 4S6.3 8.5 5.5 8.5 4.5 11.5 3.7 11.5 2.6 9.5 2.3 7.5C2 5.5 1 4.5 1 2.5z" fill="currentColor"/></svg>STRENGTHEN TEETH</li>
    </ul>
  </section>
</body>
</html>
```